Business card - Harbourline Stoneworks

Design a business card utilizing the given logo.
colors we like: Black, greys, Teal, blues.
Tri color card, horizontal orientation likely
Logo and name likely best on top.
Info on card:

Dennis Farrowby
#5 - 4180 Maple Ridge Blvd.
Surrey, B.C. V3K 2R9

778.555.0193
dennisfarrowby@brellnet.ca

Slogan: "Shaping Homes"

We are a construction company that specializes in new home construction on the West coast of BC Canada. Open Concepts designs of high end homes.

```html
<!DOCTYPE html>
<html lang="en">
<head>
<meta charset="utf-8">
<title>Harbourline Stoneworks — Business Card</title>
<link rel="stylesheet" href="https://fonts.googleapis.com/css2?family=Michroma&family=Roboto:wght@400;500&display=swap">
<style>
  :root {
    --backdrop: #2a2a2c;
    --card: #1b1b1d;
    --teal: #1fb3c8;
    --teal-deep: #178a98;
    --grey-light: #d9dadc;
    --grey-mid: #b4b6b8;
    --mark-faint: #2e4a4e;
  }
  * { box-sizing: border-box; margin: 0; padding: 0; }
  html, body {
    width: 1200px;
    height: 1000px;
    overflow: hidden;
    background: var(--backdrop);
  }
  .stage {
    width: 1200px;
    height: 1000px;
    display: flex;
    align-items: center;
    justify-content: center;
  }
  .business-card {
    position: relative;
    width: 900px;
    height: 514px;
    background: var(--card);
    overflow: hidden;
    box-shadow: 0 20px 50px rgba(0,0,0,.55);
  }
  .accent-stripe {
    position: absolute;
    left: 26px;
    top: 0;
    width: 14px;
    height: 100%;
    background: var(--teal);
  }
  .faint-mark {
    position: absolute;
    right: -110px;
    top: 150px;
    width: 330px;
    height: 330px;
  }
  .brand-block {
    position: absolute;
    left: 80px;
    top: 56px;
    display: flex;
    align-items: center;
    gap: 26px;
  }
  .brand-dot {
    width: 104px;
    height: 104px;
    border-radius: 50%;
    background: var(--teal-deep);
    flex: none;
  }
  .brand-text {
    display: flex;
    flex-direction: column;
    align-items: flex-end;
  }
  .brand-name {
    font-family: "Michroma", sans-serif;
    font-weight: 400;
    color: var(--teal);
    font-size: 38px;
    line-height: 1.15;
    letter-spacing: 1px;
    text-transform: uppercase;
  }
  .slogan {
    margin-top: 12px;
    font-family: "Roboto", sans-serif;
    font-style: italic;
    font-size: 24px;
    letter-spacing: 3px;
    color: var(--teal);
  }
  .contact {
    position: absolute;
    left: 90px;
    top: 268px;
    font-family: "Roboto", sans-serif;
  }
  .contact-name {
    font-size: 28px;
    font-weight: 500;
    letter-spacing: 2px;
    color: var(--teal);
    text-transform: uppercase;
    margin-bottom: 28px;
  }
  .contact-line {
    font-size: 21px;
    line-height: 1.3;
    color: var(--grey-light);
    letter-spacing: .5px;
  }
  .contact-line .label { color: var(--teal); margin-right: 6px; }
  .address {
    margin-top: 20px;
    font-style: normal;
    font-size: 21px;
    line-height: 1.3;
    letter-spacing: .5px;
  }
  .address .street { color: var(--grey-light); }
  .address .city { color: var(--grey-mid); }
</style>
</head>
<body>
<main class="stage">
  <section class="business-card">
    <div class="accent-stripe"></div>
    <svg class="faint-mark" viewBox="0 0 330 330" aria-hidden="true">
      <circle cx="165" cy="165" r="165" fill="var(--mark-faint)"/>
    </svg>

    <header class="brand-block">
      <div class="brand-dot"></div>
      <div class="brand-text">
        <h1 class="brand-name">Harbourline<br>Stoneworks</h1>
        <p class="slogan">“SHAPING HOMES”</p>
      </div>
    </header>

    <div class="contact">
      <h2 class="contact-name">Dennis Farrowby</h2>
      <p class="contact-line"><span class="label">P:</span>778.555.0193</p>
      <p class="contact-line"><span class="label">E:</span>dennisfarrowby@brellnet.ca</p>
      <address class="address">
        <span class="street">#5 - 4180 Maple Ridge Blvd.</span><br>
        <span class="city">Surrey, B.C. V3K 2R9</span>
      </address>
    </div>
  </section>
</main>
</body>
</html>
```